Stick and Box Packaging for Coffee

We are looking to have tube and stick designs (packaging) for our coffee product.
Use these two different kinds of packaging for your design references.

1. http://www.plivorant.com/market-we-serve/beverages/coffee
2. http://www.grabomix.com/reclosable-tubes.html

Please include a RED color somewhere on the design. May be a border line or just come up with the design. Please see the attached images as reference.

Estimated Dimension:
1. Height - 0.88 inches
2. Length - 4.50 inches

sample color palettes:
Brown
Black
Red
Green
Golden Brown

*Please make the packaging look like a premium/high end packaging.

For the meantime - please use "Tundra Coffee" as the brand name also make a sample logo for it. For the Nutrifacts and other write up, just use a sample information.

By the way, this product is VERDAmark and FRAB Organic Certified. Please do not add the nutrifacts on the sticks just write it on the box. Make the box the same design as Quelvane cigarette and the color texture a mix of glossy and matte texture.

Please use the images from this link as your additional reference for the stick and box sizes and other information

http://shpq.to/7KuwPmd

Happy New Year and Happy Designing!!!

Target Market(s)

High End and Upscale consumers

Industry/Entity Type

Product

Requirements
Must have
• Sample logo - you can use any logo just for the design then once we have the final logo I will send it to the winner.
• Additional info: Please showcase the Stick design on the box as well like the one from the Coconut Sugar packaging but make some originality with the design on are you going to showcase that on the box
Nice to have
• Please create a sample logo for "Tundra Coffee". This is not the final brand that is why we don't want to create a permanent logo. Just a placeholder Logo will do for now - any - so long as it is relevant - and especially not using known brands.

```html
<!DOCTYPE html>
<html lang="en">
<head>
<meta charset="utf-8">
<title>Tundra Coffee – Stick Packaging</title>
<link rel="stylesheet" href="https://fonts.googleapis.com/css2?family=Righteous&display=swap">
<style>
  :root {
    --paper: #ffffff;
    --frame-line: #3a3a3a;
    --bean-dark: #2a140b;
    --bean-mid: #5a2e18;
    --bean-light: #7a4226;
    --band-red: #c8321c;
    --band-orange: #e0782a;
    --band-gold: #f2c25a;
    --brand-gold: #e8b56a;
    --stick-edge: #1c0d06;
  }
  html, body {
    margin: 0;
    padding: 0;
    width: 1200px;
    height: 1200px;
    overflow: hidden;
    background: var(--paper);
  }
  .canvas {
    position: relative;
    width: 1200px;
    height: 1200px;
    box-sizing: border-box;
    border: 2px solid var(--frame-line);
    background: var(--paper);
  }
  .stick {
    position: absolute;
    left: 74px;
    top: 495px;
    width: 1052px;
    height: 208px;
    display: flex;
    box-sizing: border-box;
    border: 2px solid var(--stick-edge);
    overflow: hidden;
  }
  .stick__beans {
    flex: 0 0 178px;
    height: 100%;
    background: radial-gradient(ellipse at 45% 40%, var(--bean-light) 0%, var(--bean-mid) 45%, var(--bean-dark) 100%);
  }
  .stick__band {
    flex: 0 0 20px;
    height: 100%;
    background: linear-gradient(90deg, var(--bean-dark) 0%, var(--band-red) 25%, var(--band-orange) 50%, var(--band-gold) 62%, var(--band-red) 80%, var(--bean-dark) 100%);
  }
  .stick__face {
    position: relative;
    flex: 1 1 auto;
    height: 100%;
    display: flex;
    align-items: center;
    justify-content: center;
  }
  .stick__face-bg {
    position: absolute;
    inset: 0;
    background: radial-gradient(ellipse at 50% 50%, #6a3a22 0%, #4a2414 55%, #2e160b 100%);
  }
  .brand-name {
    position: relative;
    margin: 0;
    font-family: "Righteous", sans-serif;
    font-weight: 400;
    font-size: 92px;
    line-height: 1;
    letter-spacing: 1px;
    color: var(--brand-gold);
    white-space: nowrap;
  }
</style>
</head>
<body>
  <main class="canvas">
    <section class="stick" aria-label="Tundra Coffee stick pack">
      <div class="stick__beans" role="img" aria-label="Close-up photo of roasted coffee beans"></div>
      <div class="stick__band" role="img" aria-label="Red and gold zigzag ornamental band"></div>
      <div class="stick__face">
        <div class="stick__face-bg" role="img" aria-label="Soft-focus background of roasted coffee beans"></div>
        <h1 class="brand-name">Tundra Coffee</h1>
      </div>
      <div class="stick__band" role="img" aria-label="Red and gold zigzag ornamental band"></div>
      <div class="stick__beans" role="img" aria-label="Close-up photo of roasted coffee beans"></div>
    </section>
  </main>
</body>
</html>
```